Off Grid consulting and outdoor products needs a website

We need a website design to help launch our new business. Its a business that plans to offer Off-grid conslting and outdoor survival products to people who are looking to relocate or vacation to properties/homes that are Off-grid. We plan to offer design plans for homes/cabins, renewable energy systems for power/heating etc, survival products for outdoor vacations/living. We also do consulting and project management for those who want to design and build from scratch their dream off-grid home or vacation property. I've included our logo design for use.
Would like the website to include 5 pages.
www.bramblequietlands.com
The main landing page (1)
want a video loop backround with a flyover of a cabin in the woods.
https://www.clipvaultmedia.com/video/clip-48213307-pale-sky-thawing-frost-on-pine-slope
(also need a backup static image of just high-shot of cabin in woods)
logo top left, Quoted string of text in the middle, over the video. and a CTA button to 'Contact us'
picture links below that to last 3 recent blog posts.
About Us page (2)
(example) https://larkhollowgear.com/pages/about-lark
Blog page (3)
blog posts associated with pictures.
Consulting 'services' page (4)
-land services and moving off-grid
-Building off grid
-Renewable energy off-grid
-Sustainable farming and all season greenhouses
Store page 'comming soon' (5)
(Example) http://hearthkeep.quillstheme.com/demo-1/demo.html

Target Market(s)

Outdoor enthusiasts and people who want to escape their city life

Coding

Coded - Design and coding required

Requirements
Must have
• Outdoor feel, woods, cabin, reneable energy (solar, geothermal, greenhouses, water wells)

```html
<!DOCTYPE html>
<html lang="en">
<head>
<meta charset="utf-8">
<title>Bramble Quietlands – Home Page Concepts</title>
<link rel="stylesheet" href="https://fonts.googleapis.com/css2?family=Oswald:wght@600;700&family=Roboto:wght@400;500;700&display=swap">
<style>
:root{
  --stage:#c6c6c6;
  --forest-deep:#0a160c;
  --forest:#15241a;
  --moss:#5c6a59;
  --moss-light:#6f7d6b;
  --ink:#111;
  --muted:#7a7a7a;
  --white:#fff;
  --wood:#8a6a45;
  --wood-light:#b08a5c;
  --heading:'Oswald',sans-serif;
  --body:'Roboto',sans-serif;
}
*{box-sizing:border-box;margin:0;padding:0}
html,body{width:1200px;height:934px;overflow:hidden}
body{background:var(--stage);font-family:var(--body);position:relative;color:var(--ink)}
.page{position:absolute;top:86px;width:511px;background:var(--white);overflow:hidden}
.page--framed{left:65px;height:761px}
.page--wave{left:623px;height:737px}
.abs{position:absolute}

/* brand mark */
.brand{display:flex;align-items:center;gap:4px;font-family:var(--body);font-weight:700;text-transform:uppercase;color:var(--white);line-height:1.05}
.brand__dot{width:10px;height:10px;border-radius:50%;background:var(--white);flex:none}

/* nav */
.nav{display:flex;gap:17px;font-size:6px;font-weight:700;letter-spacing:.1px}
.nav--light{color:var(--white)}
.nav--dark{color:var(--ink)}

/* hero text */
.hero-title{font-family:var(--heading);font-style:italic;font-weight:700;text-transform:uppercase;font-size:21px;letter-spacing:.3px;text-align:center;color:var(--white);width:100%}
.hero-lede{font-size:7.4px;font-weight:500;line-height:12px;text-align:center;color:var(--white);width:100%}
.pill{display:flex;align-items:center;justify-content:center;gap:4px;background:var(--moss);color:var(--white);font-weight:500;font-size:7px;border-radius:12px;text-transform:uppercase}
.pill__arrow{width:6px;height:6px;border-radius:50%;background:var(--white);position:relative}
.pill__arrow::after{content:"";position:absolute;left:2px;top:1.5px;border-left:2.5px solid var(--moss);border-top:1.5px solid transparent;border-bottom:1.5px solid transparent}

.play{width:38px;height:38px;border-radius:50%;background:#0c0c0c;border:2px solid #2a3a2c;display:flex;align-items:center;justify-content:center}
.play::after{content:"";border-left:11px solid var(--white);border-top:7px solid transparent;border-bottom:7px solid transparent;margin-left:3px}

/* blog */
.section-title{font-family:var(--heading);font-style:italic;font-weight:700;font-size:22px;text-transform:uppercase;text-align:center;width:100%;color:var(--ink)}
.cards{display:flex;gap:11px;left:48px}
.card{width:131px;height:165px;background:var(--white);border-radius:5px;box-shadow:0 1px 5px rgba(0,0,0,.1);padding:3px;text-align:center}
.card__photo{height:86px;border-radius:3px}
.card__photo--a{background:linear-gradient(180deg,#3f6fb5 0%,#7ea6d4 40%,#a57b52 70%,#3c3a30 100%)}
.card__photo--b{background:linear-gradient(180deg,#2a65c1 0%,#6d8fb8 35%,#7a7f86 60%,#8d4f36 100%)}
.card__photo--c{background:linear-gradient(180deg,#2f5a2b 0%,#5b8a3a 40%,#b58a3f 65%,#3a5e8a 80%,#4f8a36 100%)}
.card__date{margin-top:11px;font-size:5.8px;color:var(--muted);display:flex;align-items:center;justify-content:center;gap:2px}
.card__date::before{content:"";width:5px;height:5px;border:1px solid var(--muted);border-radius:1px}
.card__title{margin-top:3px;font-size:7.2px;font-weight:500;color:var(--ink)}
.card__text{margin-top:4px;font-size:6px;line-height:9.5px;color:var(--muted);padding:0 6px}
.card__more{margin-top:5px;font-size:6.3px;font-weight:500;color:var(--moss);display:flex;align-items:center;justify-content:center;gap:3px}
.card__more .pill__arrow{background:var(--moss);width:5.5px;height:5.5px}
.card__more .pill__arrow::after{border-left-color:var(--white);left:1.8px;top:1.3px}

/* footer */
.footer{left:0;width:511px;background:var(--forest-deep);color:var(--white)}
.footer h4{font-size:7px;font-weight:500;margin-bottom:9px}
.footer__col{font-size:5.7px;line-height:11px}
.contact-item{display:flex;gap:6px;margin-bottom:5px;line-height:7.5px}
.contact-item b{display:block;font-size:5px;font-weight:700}
.contact-item svg{flex:none;margin-top:1px}
.questions p{font-size:5.4px;line-height:8px;margin-bottom:11px}
.social{display:flex;gap:9px}
.social span{width:6px;height:6px;border-radius:50%;background:var(--white)}
.go-up{background:var(--forest);border:1px solid #243226;border-radius:6px;font-size:4.8px;font-weight:700;padding:1.5px 5px;display:flex;gap:2px;align-items:center}
.go-up::before{content:"";border-bottom:3px solid var(--white);border-left:2px solid transparent;border-right:2px solid transparent}
.rule{height:0;border-top:1px dashed #26332a}
.legal{font-size:5.8px;display:flex;justify-content:space-between}
.legal nav{display:flex;gap:4px}
</style>
</head>
<body>

<!-- Concept one: framed video -->
<section class="page page--framed">
  <div class="abs" style="left:0;top:0;width:511px;height:255px;background:linear-gradient(160deg,#1c2a1d 0%,#0f1a10 45%,#223023 75%,#101a11 100%)" role="img" aria-label="Darkened photo of a forest cabin at night"></div>

  <div class="abs brand" style="left:48px;top:16px;font-size:9px;width:60px">
    <span class="brand__dot"></span><span>Bramble<br>Quietlands</span>
  </div>
  <nav class="abs nav nav--light" style="left:246px;top:26px">
    <span>HOME</span><span>ABOUT US</span><span>BLOG</span><span>CONSULTING SERVICES</span><span>STORE</span>
  </nav>

  <h1 class="abs hero-title" style="left:0;top:61px">Bramble Quietlands</h1>
  <p class="abs hero-lede" style="left:0;top:94px">Lorem ipsum dolor sit amet, consectetur adipiscing elit, sed do eiusmod<br>tempor incididunt ut labore et dolore magna aliqua.</p>
  <div class="abs pill" style="left:211px;top:127px;width:89px;height:22px">Contact us <span class="pill__arrow"></span></div>

  <div class="abs" style="left:105px;top:170px;width:301px;height:165px;border:10px solid var(--wood);outline:1px solid var(--wood-light);background:var(--wood)">
    <div style="width:100%;height:100%;background:linear-gradient(180deg,#4f7fc4 0%,#c9d9ec 25%,#9ea6a9 45%,#4d5445 70%,#2c3a2c 100%)" role="img" aria-label="Video still: aerial flyover of a cabin among snowy pines and mountains"></div>
  </div>
  <div class="abs play" style="left:237px;top:233px"></div>

  <h2 class="abs section-title" style="left:0;top:363px">Recent Blog</h2>
  <div class="abs cards" style="top:402px">
    <article class="card"><div class="card__photo card__photo--a" role="img" aria-label="Modern solar-roofed house at dusk"></div><div class="card__date">April 12, 2020</div><div class="card__title">Lorem ipsum dolor sit amet,</div><p class="card__text">Sed ut perspiciatis unde omnis iste natus error voluptatem accusantium</p><div class="card__more">READ MORE <span class="pill__arrow"></span></div></article>
    <article class="card"><div class="card__photo card__photo--b" role="img" aria-label="Grey house with solar panels and a deck"></div><div class="card__date">April 12, 2020</div><div class="card__title">Lorem ipsum dolor sit amet,</div><p class="card__text">Sed ut perspiciatis unde omnis iste natus error voluptatem accusantium</p><div class="card__more">READ MORE <span class="pill__arrow"></span></div></article>
    <article class="card"><div class="card__photo card__photo--c" role="img" aria-label="Timber cabin with green roof and solar array"></div><div class="card__date">April 12, 2020</div><div class="card__title">Lorem ipsum dolor sit amet,</div><p class="card__text">Sed ut perspiciatis unde omnis iste natus error voluptatem accusantium</p><div class="card__more">READ MORE <span class="pill__arrow"></span></div></article>
  </div>

  <footer class="abs footer" style="top:607px;height:154px">
    <div class="abs brand" style="left:49px;top:35px;font-size:13px;width:80px"><span class="brand__dot"></span><span>Bramble<br>Quietlands</span></div>
    <div class="abs social" style="left:66px;top:107px"><span></span><span></span><span></span><span></span></div>

    <div class="abs footer__col" style="left:169px;top:32px">
      <h4>Our Office Address</h4>
      <div class="contact-item"><svg width="5" height="5" viewBox="0 0 10 10"><path d="M2 0l2 2-1 2 3 3 2-1 2 2-2 2C4 10 0 6 0 2z" fill="#9aa"/></svg><div><b>Phone</b>+1 888 888 8888</div></div>
      <div class="contact-item"><svg width="6" height="5" viewBox="0 0 12 9"><rect width="12" height="9" fill="#9aa"/><path d="M0 0l6 5 6-5" stroke="#0a160c" fill="none"/></svg><div><b>Email</b>info@bramblequietlands.com</div></div>
      <div class="contact-item"><svg width="5" height="6" viewBox="0 0 10 12"><path d="M5 12S0 6 0 4a5 5 0 0110 0c0 2-5 8-5 8z" fill="#9aa"/></svg><div><b>Location</b>767 Lorem ipsum dolor sit amet,<br>consectetur adipiscing elit</div></div>
    </div>
    <div class="abs footer__col" style="left:298px;top:32px">
      <h4>Company</h4>
      <div>Home</div><div>About Us</div><div>Blog</div><div>Consulting Services</div><div>Store</div>
    </div>
    <div class="abs footer__col questions" style="left:368px;top:32px;width:100px">
      <h4>Stil have questios?</h4>
      <p>Contact us using this form. A repesenta-tive will aswer your questions as soon as possible.</p>
      <div class="pill" style="width:85px;height:18px;border-radius:9px">Get a quote</div>
    </div>
    <div class="abs rule" style="left:48px;top:125px;width:416px"></div>
    <div class="abs go-up" style="left:431px;top:120px">Go Up</div>
    <div class="abs legal" style="left:48px;top:136px;width:416px"><span>© 2021  bramblequietlands | All Rights Reserved</span><nav><span>Privacy Policy</span>|<span>Cookie Policy</span>|<span>Terms Of Services</span></nav></div>
  </footer>
</section>

<!-- Concept two: full-bleed hero with waves -->
<section class="page page--wave">
  <div class="abs" style="left:0;top:36px;width:511px;height:275px;background:linear-gradient(180deg,#3f73b8 0%,#b9cce0 28%,#8d9597 48%,#4b5346 70%,#2a3a2d 100%)" role="img" aria-label="Aerial flyover video of a cabin among snowy pines and mountains"></div>
  <svg class="abs" style="left:0;top:270px" width="511" height="60" viewBox="0 0 511 60" preserveAspectRatio="none">
    <path d="M0 10 C80 28 160 30 260 22 S420 12 511 34 V60 H0Z" fill="var(--moss)"/>
    <path d="M0 16 C80 34 160 36 260 28 S420 18 511 40 V60 H0Z" fill="var(--white)"/>
  </svg>

  <div class="abs" style="left:0;top:0;width:511px;height:36px;background:var(--white)"></div>
  <div class="abs" style="left:46px;top:-16px;width:80px;height:80px;border-radius:50%;background:var(--white)"></div>
  <div class="abs brand" style="left:60px;top:14px;font-size:9.5px;color:var(--ink);width:60px">
    <span class="brand__dot" style="background:var(--ink)"></span><span>Bramble<br>Quietlands</span>
  </div>
  <nav class="abs nav nav--dark" style="left:246px;top:15px">
    <span>HOME</span><span>ABOUT US</span><span>BLOG</span><span>CONSULTING SERVICES</span><span>STORE</span>
  </nav>

  <div class="abs play" style="left:237px;top:76px"></div>
  <h1 class="abs hero-title" style="left:0;top:124px">Bramble Quietlands</h1>
  <p class="abs hero-lede" style="left:0;top:159px">Lorem ipsum dolor sit amet, consectetur adipiscing elit, sed do eiusmod<br>tempor incididunt ut labore et dolore magna aliqua.</p>
  <div class="abs pill" style="left:211px;top:191px;width:89px;height:22px">Contact us <span class="pill__arrow"></span></div>

  <h2 class="abs section-title" style="left:0;top:327px">Recent Blog</h2>
  <div class="abs cards" style="top:364px">
    <article class="card"><div class="card__photo card__photo--a" role="img" aria-label="Modern solar-roofed house at dusk"></div><div class="card__date">April 12, 2020</div><div class="card__title">Lorem ipsum dolor sit amet,</div><p class="card__text">Sed ut perspiciatis unde omnis iste natus error voluptatem accusantium</p><div class="card__more">READ MORE <span class="pill__arrow"></span></div></article>
    <article class="card"><div class="card__photo card__photo--b" role="img" aria-label="Grey house with solar panels and a deck"></div><div class="card__date">April 12, 2020</div><div class="card__title">Lorem ipsum dolor sit amet,</div><p class="card__text">Sed ut perspiciatis unde omnis iste natus error voluptatem accusantium</p><div class="card__more">READ MORE <span class="pill__arrow"></span></div></article>
    <article class="card"><div class="card__photo card__photo--c" role="img" aria-label="Timber cabin with green roof and solar array"></div><div class="card__date">April 12, 2020</div><div class="card__title">Lorem ipsum dolor sit amet,</div><p class="card__text">Sed ut perspiciatis unde omnis iste natus error voluptatem accusantium</p><div class="card__more">READ MORE <span class="pill__arrow"></span></div></article>
  </div>

  <svg class="abs" style="left:0;top:555px" width="511" height="46" viewBox="0 0 511 46" preserveAspectRatio="none">
    <path d="M0 0 C40 20 120 22 240 14 S420 10 511 30 V46 H0Z" fill="var(--moss)"/>
    <path d="M0 6 C40 26 120 28 240 20 S420 16 511 36 V46 H0Z" fill="var(--forest-deep)"/>
  </svg>
  <footer class="abs footer" style="top:600px;height:137px">
    <div class="abs brand" style="left:50px;top:16px;font-size:13px;width:80px"><span class="brand__dot"></span><span>Bramble<br>Quietlands</span></div>
    <div class="abs social" style="left:66px;top:87px"><span></span><span></span><span></span><span></span></div>

    <div class="abs footer__col" style="left:169px;top:10px">
      <h4>Our Office Address</h4>
      <div class="contact-item"><svg width="5" height="5" viewBox="0 0 10 10"><path d="M2 0l2 2-1 2 3 3 2-1 2 2-2 2C4 10 0 6 0 2z" fill="#9aa"/></svg><div><b>Phone</b>+1 888 888 8888</div></div>
      <div class="contact-item"><svg width="6" height="5" viewBox="0 0 12 9"><rect width="12" height="9" fill="#9aa"/><path d="M0 0l6 5 6-5" stroke="#0a160c" fill="none"/></svg><div><b>Email</b>info@bramblequietlands.com</div></div>
      <div class="contact-item"><svg width="5" height="6" viewBox="0 0 10 12"><path d="M5 12S0 6 0 4a5 5 0 0110 0c0 2-5 8-5 8z" fill="#9aa"/></svg><div><b>Location</b>767 Lorem ipsum dolor sit amet,<br>consectetur adipiscing elit</div></div>
    </div>
    <div class="abs footer__col" style="left:298px;top:10px">
      <h4>Company</h4>
      <div>Home</div><div>About Us</div><div>Blog</div><div>Consulting Services</div><div>Store</div>
    </div>
    <div class="abs footer__col questions" style="left:368px;top:10px;width:100px">
      <h4>Stil have questios?</h4>
      <p>Contact us using this form. A repesenta-tive will aswer your questions as soon as possible.</p>
      <div class="pill" style="width:85px;height:18px;border-radius:9px">Get a quote</div>
    </div>
    <div class="abs rule" style="left:48px;top:105px;width:416px"></div>
    <div class="abs go-up" style="left:431px;top:100px">Go Up</div>
    <div class="abs legal" style="left:48px;top:116px;width:416px"><span>© 2021  bramblequietlands | All Rights Reserved</span><nav><span>Privacy Policy</span>|<span>Cookie Policy</span>|<span>Terms Of Services</span></nav></div>
  </footer>
</section>

</body>
</html>
```